依頼詳細
スパ(ラポルト ミルネ表参道)のお客様向けのDMの作成をお願いいたします。
シンプルで洗練されたデザインでお願いいたします。期間限定の特別トリートメントの訴求です。写真のイメージに合わせたテイストでお願いします。

文字が多いのですが、すっきりと分かりやすくしていただけると幸いです。

本依頼の際に画像の本データは送付いたします。
記載項目
中面:プロモーション内容
宛名面:告知文
希望イメージ
シンプル 複雑
単色 カラフル
暗い 明るい
日常 高級
遊び心 厳粛
未来的 伝統的
女性的 男性的
希望する色
写真に合わせてゴールドを中心に、プラスするなら深いグリーンをでお願いします
納品ファイル
• 高解像度JPG (.jpg)
• イラストレーター形式 (.ai)
補足説明

ブランドのイメージにあったため当選させていただきました。

沢山のご応募ありがとうございました。引き続きどうぞよろしくお願いいたします。

```html
<!DOCTYPE html>
<html lang="ja">
<head>
<meta charset="UTF-8">
<title>ノルダ ヒーリング スパプログラム｜ラポルト ミルネ表参道</title>
<link rel="stylesheet" href="https://fonts.googleapis.com/css2?family=Shippori+Mincho:wght@400;600;700&family=Noto+Serif+JP:wght@400;600&display=swap">
<style>
  :root{
    --gold:#c2a064;
    --gold-light:#e4cf9f;
    --gold-band:#ece0c6;
    --forest:#1e3628;
    --ink:#3b2d20;
    --paper:#fbf8f2;
    --photo-dark:#140d08;
  }
  *{margin:0;padding:0;box-sizing:border-box;}
  html,body{width:808px;height:1200px;overflow:hidden;background:var(--paper);}
  .dm{position:relative;width:808px;height:1200px;background:var(--paper);font-family:"Noto Serif JP",serif;color:var(--ink);}

  .hero{position:absolute;left:0;top:0;width:808px;height:810px;
    background:
      radial-gradient(ellipse 60% 40% at 68% 42%, #8a5a36 0%, rgba(107,68,40,.6) 40%, rgba(20,13,8,0) 75%),
      radial-gradient(ellipse 22% 20% at 18% 76%, #efe6d6 0%, rgba(200,180,150,.5) 50%, rgba(20,13,8,0) 85%),
      linear-gradient(160deg, #3a2a1c 0%, var(--photo-dark) 55%, #0c0805 100%);}

  .season-badge{position:absolute;left:13px;top:13px;width:196px;height:190px;background:var(--forest);
    display:flex;flex-direction:column;align-items:center;justify-content:center;
    font-family:"Shippori Mincho",serif;font-weight:600;color:#fff;font-size:26px;line-height:1.6;letter-spacing:.04em;}
  .season-badge svg{position:absolute;inset:0;}
  .season-badge span{position:relative;}

  .hero-title{position:absolute;left:440px;top:480px;width:360px;
    font-family:"Shippori Mincho",serif;font-weight:600;color:var(--gold-light);
    font-size:38px;line-height:2;letter-spacing:.08em;}
  .hero-lead{position:absolute;left:470px;top:712px;width:330px;
    font-family:"Shippori Mincho",serif;color:#f2eadc;font-size:14px;line-height:1.9;letter-spacing:.02em;}

  .menu{position:absolute;left:0;top:810px;width:808px;padding:0 20px;}
  .treatment{margin-top:14px;}
  .treatment + .treatment{margin-top:24px;}
  .treatment-head{display:flex;justify-content:space-between;align-items:flex-end;
    padding:3px 6px;border-bottom:5px solid var(--gold-band);
    font-family:"Shippori Mincho",serif;font-weight:700;font-size:16px;letter-spacing:.06em;color:var(--ink);}
  .treatment-price{font-weight:600;font-size:15px;}
  .treatment-text{margin-top:8px;padding:0 6px;font-size:14px;line-height:1.75;letter-spacing:.02em;text-align:justify;}
</style>
</head>
<body>
<main class="dm">
  <div class="hero" role="img" aria-label="キャンドルのオイルを背中に垂らしてマッサージを受ける女性と、左下にトリートメントオイルキャンドルの製品写真"></div>

  <div class="season-badge">
    <svg width="196" height="190" viewBox="0 0 196 190" aria-hidden="true">
      <rect x="7" y="7" width="182" height="176" fill="none" stroke="var(--gold)" stroke-width="1.5"/>
      <rect x="11" y="11" width="174" height="168" fill="none" stroke="var(--gold)" stroke-width="0.8"/>
    </svg>
    <span>2019年冬限定</span>
    <span>トリートメント</span>
    <span>12/1(日)より</span>
  </div>

  <h1 class="hero-title">ノルダ ヒーリング<br>スパプログラム</h1>
  <p class="hero-lead">トリートメントオイル キャンドルで、<br>深い安らぎ、深い森に抱かれているような温もりを</p>

  <section class="menu">
    <article class="treatment">
      <h2 class="treatment-head"><span>ノルダ ホットオイル キャンドルトリートメント</span><span class="treatment-price">60分 / 19,800円</span></h2>
      <p class="treatment-text">「ノルダ」とは、北の大地に広がる針葉樹林をイメージした名であり、樹齢500年にも及ぶ木々が生い茂る、とても神聖な場所。キャンドルから溶け出したオイルの温もりと森の温かい香りが心地良いボディトリートメントで極上のリラックスタイムへ導きます。</p>
    </article>
    <article class="treatment">
      <h2 class="treatment-head"><span>ノルダ ホットストーン キャンドルトリートメント</span><span class="treatment-price">90分 / 26,400円</span></h2>
      <p class="treatment-text">キャンドルオイルと自然石を使ったストーンボディセラピー。自然の力と共鳴する極上のリラクゼーショントリートメント。</p>
    </article>
    <article class="treatment">
      <h2 class="treatment-head"><span>ノルダ ホットオイル キャンドルトリートメント Premium</span><span class="treatment-price">120分 / 33,000円</span></h2>
      <p class="treatment-text">キャンドルトリートメントにエイジングケアフェイシャルをプラスした、心と身体の解放と輝く肌へと導く贅沢なコース。</p>
    </article>
  </section>
</main>
</body>
</html>
```